Gelato Business Card

create a new business card using existing logo

Target Market(s)

B2B

Contact Information for Business Card

typical contact info: logo, address, email, phone, rep name

Colors
0355a3
33a6d7

Requirements
Must have
• a feel of high quality, luxury, happiness
• use cool, comforting color and texture of business card.
Nice to have
• "Crafted Slowly, Savoured Every Day!" TM
• or, "more quality, more flavor"
• or, "Flavor Matters"

```html
<!DOCTYPE html>
<html lang="en">
<head>
<meta charset="utf-8">
<title>Bellamonte Business Card</title>
<link rel="stylesheet" href="https://fonts.googleapis.com/css2?family=Roboto:wght@400;500&family=Raleway:wght@400&display=swap">
<style>
  :root {
    --card-paper: #e8e7e4;
    --card-paper-light: #efeeeb;
    --brand-navy: #3f4396;
    --tagline-orange: #e07a3c;
    --text-grey: #56575a;
  }
  html, body {
    margin: 0;
    padding: 0;
    width: 1200px;
    height: 794px;
    overflow: hidden;
    background: #ffffff;
  }
  .business-card {
    position: relative;
    width: 1200px;
    height: 794px;
    background: radial-gradient(ellipse at 60% 40%, var(--card-paper-light), var(--card-paper) 75%);
    font-family: "Roboto", Arial, sans-serif;
  }
  .brand-block {
    position: absolute;
    top: 105px;
    right: 110px;
    text-align: right;
  }
  .brand-name {
    display: flex;
    align-items: center;
    justify-content: flex-end;
    gap: 16px;
    margin: 0;
    font-weight: 500;
    font-size: 56px;
    letter-spacing: 1px;
    color: var(--brand-navy);
    text-transform: uppercase;
  }
  .brand-dot {
    width: 24px;
    height: 24px;
  }
  .tagline {
    margin: 40px 0 0;
    font-family: "Raleway", Arial, sans-serif;
    font-weight: 400;
    font-size: 22px;
    letter-spacing: 0.5px;
    color: var(--tagline-orange);
    text-transform: uppercase;
  }
  .contact-block {
    position: absolute;
    left: 90px;
    bottom: 110px;
  }
  .rep-name {
    margin: 0 0 12px;
    font-weight: 500;
    font-size: 46px;
    letter-spacing: 1px;
    color: var(--brand-navy);
    text-transform: uppercase;
  }
  .contact-line {
    margin: 0;
    font-weight: 400;
    font-size: 31px;
    line-height: 1.4;
    color: var(--text-grey);
  }
</style>
</head>
<body>
  <main class="business-card">
    <header class="brand-block">
      <p class="brand-name">
        <svg class="brand-dot" viewBox="0 0 24 24" aria-hidden="true">
          <circle cx="12" cy="12" r="12" fill="#3f4396"/>
        </svg>
        Bellamonte
      </p>
      <p class="tagline">Crafted Slowly, Savoured Every Day</p>
    </header>
    <section class="contact-block">
      <h1 class="rep-name">Clara Vance</h1>
      <p class="contact-line">412 Larkspur Road, Juneau, Alaska 99801</p>
      <p class="contact-line">907 555 0142 | clara@bellamonte.com | www.bellamonte.com</p>
    </section>
  </main>
</body>
</html>
```